South Florida Real Estate Brokerage Business

The name is DWELL VANTORO REAL ESTATE.
The company is a Real estate realty based in Miami.
Is targeted to Latin American clients.
Must express luxury, and efficiency.
Target clients for properties around 250k to a million +.
Vantoro means Royal in Latin.
Should communicate safety and knowledge of the product and transaction with a tech edge.

The web design needs to be a Social tool, with Chatterloop and other media integration of some sort. Needs to have a Show case place, a Search place (MLS listings) with maps and filters.
Needs to reflect luxury but also mixed with a social edge capable of engaging clients or transition them to communicate with the page.
Include the logo from the uploaded files, feel free to change the color or font per webdesign.
This is a Front en design, layout and graphics.
Possible future programming if approved.
I can receive Quotes for the Code part.

Target Market(s)

Spanish and English speakers living in Latin America and Canada looking for apartments and houses to buy.

Industry/Entity Type

Business

Requirements
Must have
• Search area.
Neighbourhood area.
Could be a blog or news area.
Client registration.
Social Plugin
Nice to have
• Social linking to networks.
Log in with chatterloop account.
Chatterloop Like.

```html
<!DOCTYPE html>
<html lang="en">
<head>
<meta charset="utf-8">
<title>Dwell Vantoro Real Estate</title>
<link href="https://fonts.googleapis.com/css2?family=Gelasio:ital,wght@0,400;0,700;1,400&family=Open+Sans:wght@400;600&display=swap" rel="stylesheet">
<style>
:root{
  --ink:#231a17;
  --gold:#c8ad69;
  --gold-light:#e8d49e;
  --cream:#ead9ad;
  --white:#fff;
  --text:#2b2522;
  --rule:#c9c2b8;
}
*{box-sizing:border-box;margin:0;padding:0}
html,body{width:817px;height:1200px;overflow:hidden;background:var(--white)}
body{position:relative;font-family:"Open Sans",Arial,sans-serif;color:var(--text)}
.abs{position:absolute}
.serif{font-family:"Gelasio",Georgia,serif}

/* header */
.brand{left:15px;top:0;width:163px;height:104px;text-align:center}
.brand-mark{position:absolute;left:53px;top:0;width:56px;height:55px;background:var(--gold)}
.brand-name{position:absolute;left:0;right:0;top:62px;font-family:"Gelasio",Georgia,serif;font-size:17px;letter-spacing:.5px;color:var(--ink);white-space:nowrap}
.brand-rule{position:absolute;left:0;right:0;top:86px;border-top:1px solid var(--gold)}
.brand-sub{position:absolute;left:0;right:0;top:86px;font-family:"Gelasio",Georgia,serif;font-size:12px;letter-spacing:.5px;color:var(--ink)}
.login{left:430px;top:26px;width:75px;height:15px;background:#3b5998;color:var(--white);font-size:8px;font-weight:600;line-height:15px;text-align:center;border-radius:1px}
.site-search{left:517px;top:22px;width:283px;height:22px;border:1px solid #bbb;font-size:8px;color:#888;line-height:20px;padding-left:8px}
.site-search svg{position:absolute;right:4px;top:3px}
.nav{left:381px;top:69px;width:419px;height:38px;border-top:1px solid var(--ink);display:flex;font-size:11px}
.nav a{color:var(--ink);text-decoration:none;line-height:37px;padding:0 15px}
.nav a.active{background:var(--ink);color:var(--gold-light);padding:0 17px}
.gold-band{left:0;top:107px;width:817px;height:4px;background:var(--gold)}

.hero{left:0;top:111px;width:817px;height:358px;background:linear-gradient(180deg,#9fc3e6 0%,#d9dde0 35%,#6f7c64 65%,#4f6b37 100%)}
.hero-rule{left:0;top:469px;width:817px;height:2px;background:var(--ink)}

/* search */
.search{left:15px;top:471px;width:252px;height:305px;background:var(--ink);color:var(--white)}
.search h2{position:absolute;left:20px;top:10px;font-family:"Gelasio",Georgia,serif;font-weight:400;font-size:24px;color:var(--gold)}
.label{position:absolute;font-size:11px}
.field{position:absolute;height:18px;background:var(--white)}
.field.select::after{content:"";position:absolute;right:6px;top:6px;border-left:5px solid transparent;border-right:5px solid transparent;border-top:7px solid var(--ink)}
.adv{position:absolute;left:30px;top:274px;font-family:"Gelasio",Georgia,serif;font-size:12px;color:var(--gold)}
.btn-gold{position:absolute;background:linear-gradient(180deg,#f1e0ae,#c8ad69);color:var(--ink);font-family:"Gelasio",Georgia,serif;text-align:center}
.find{left:150px;top:271px;width:76px;height:21px;line-height:21px;font-size:14px}

/* news */
.news{left:280px;top:484px;width:252px;height:292px;background:var(--gold)}
.news h2{position:absolute;left:20px;top:12px;font-family:"Gelasio",Georgia,serif;font-weight:400;font-size:22px;color:var(--ink)}
.news-item{position:absolute;left:20px;width:220px;color:var(--white);font-size:11px;line-height:14.5px}
.news-date{display:inline-block;background:var(--ink);padding:0 9px;height:15px;line-height:15px;margin-bottom:2px}
.read-more{position:absolute;left:185px;top:265px;font-family:"Gelasio",Georgia,serif;font-size:10px;color:var(--ink)}

/* register */
.register{left:548px;top:484px;width:252px;height:292px;background:var(--cream)}
.register-photo{position:absolute;left:14px;top:14px;width:223px;height:137px;background:linear-gradient(180deg,#2f5f9e,#8fb0d4 55%,#4a5d77)}
.register p{position:absolute;left:17px;top:163px;width:222px;font-size:11px;line-height:15px;color:var(--ink)}
.email{position:absolute;left:17px;top:220px;width:217px;height:20px;background:var(--white);font-family:"Gelasio",Georgia,serif;font-style:italic;font-size:11px;color:#999;padding-left:7px;line-height:20px}
.register-btn{position:absolute;left:103px;top:250px;width:131px;height:25px;background:var(--ink);color:var(--gold-light);font-family:"Gelasio",Georgia,serif;font-weight:700;font-size:14px;text-align:center;line-height:25px}

/* showcase */
.showcase-title{left:14px;top:807px;font-family:"Gelasio",Georgia,serif;font-size:22px;color:var(--ink)}
.arrow{top:912px}
.card{top:854px;width:152px}
.card-photo{width:152px;height:146px}
.card-title{margin-top:10px;font-size:11px}
.card-meta{display:flex;justify-content:space-between;font-size:11px;margin-top:1px;padding-bottom:3px;border-bottom:1px solid var(--rule);width:154px}
.details{position:relative!important;display:block;margin:9px auto 0;width:76px;height:22px;line-height:22px;font-size:12px}
.divider{top:854px;width:1px;height:224px;background:var(--rule)}

/* footer */
.footer{left:0;top:1112px;width:817px;height:88px;background:var(--ink)}
.likes{left:688px;top:1110px;width:112px;height:22px;background:var(--white);font-size:11px;line-height:22px;padding-left:9px}
.likes span{display:inline-block;border:1px solid #9aa6c1;font-size:6px;line-height:9px;padding:0 3px;margin-right:8px;vertical-align:middle;color:#3b5998}
.copyright{left:0;top:1148px;width:817px;text-align:center;font-family:"Gelasio",Georgia,serif;font-size:10px;color:var(--white)}
</style>
</head>
<body>

<header>
  <div class="abs brand">
    <div class="brand-mark"></div>
    <div class="brand-name">DWELL VANTORO</div>
    <div class="brand-rule"></div>
    <div class="brand-sub">REAL ESTATE</div>
  </div>
  <div class="abs login">Chatterloop Login</div>
  <div class="abs site-search">MLS ID, Building Name, Address, City, Zip, or Agent Name
    <svg width="14" height="14" viewBox="0 0 14 14"><circle cx="6" cy="6" r="4.5" fill="none" stroke="#231a17" stroke-width="1.6"/><line x1="9.3" y1="9.3" x2="13" y2="13" stroke="#231a17" stroke-width="1.8"/></svg>
  </div>
  <nav class="abs nav">
    <a class="active">Home</a><a>Company</a><a>Search Properties</a><a>Propeties</a><a>Contact</a>
  </nav>
  <div class="abs gold-band"></div>
</header>

<div class="abs hero" role="img" aria-label="Large white country house with dark shutters, wraparound porch and flowering gardens"></div>
<div class="abs hero-rule"></div>

<section class="abs search">
  <h2>Search</h2>
  <span class="label" style="left:27px;top:48px">City, State, or Zip</span>
  <div class="field" style="left:28px;top:65px;width:198px"></div>
  <span class="label" style="left:27px;top:92px">Location</span>
  <div class="field select" style="left:28px;top:109px;width:198px"></div>
  <span class="label" style="left:27px;top:136px">Price Range</span>
  <span class="label" style="left:138px;top:136px">To</span>
  <div class="field select" style="left:28px;top:154px;width:97px"></div>
  <div class="field select" style="left:128px;top:154px;width:98px"></div>
  <span class="label" style="left:27px;top:180px">Bedrooms</span>
  <div class="field select" style="left:28px;top:197px;width:198px"></div>
  <span class="label" style="left:27px;top:224px">Bathrooms</span>
  <div class="field select" style="left:28px;top:241px;width:198px"></div>
  <span class="adv">Advance Search</span>
  <span class="btn-gold find">Find</span>
</section>

<section class="abs news">
  <h2>News Updates</h2>
  <div class="news-item" style="top:49px"><span class="news-date">10 - 12 - 2012</span><br>Lorem Ipsum is simply dummy text of the printing and typesetting industry  and typesetting industry.</div>
  <div class="news-item" style="top:125px"><span class="news-date">10 - 12 - 2012</span><br>Lorem Ipsum is simply dummy text of the printing and typesetting industry  and typesetting industry.</div>
  <div class="news-item" style="top:197px"><span class="news-date">10 - 12 - 2012</span><br>Lorem Ipsum is simply dummy text of the printing and typesetting industry  and typesetting industry.</div>
  <span class="read-more">read more</span>
</section>

<section class="abs register">
  <div class="register-photo" role="img" aria-label="Two business people shaking hands in front of glass skyscrapers"></div>
  <p>Lorem Ipsum is simply dummy text of the printing and typesetting industry  and typesetting industry.</p>
  <div class="email">enter your email id</div>
  <div class="register-btn">Register Now</div>
</section>

<h2 class="abs showcase-title" style="font-weight:400">Property Showcase</h2>
<svg class="abs arrow" style="left:15px" width="16" height="26" viewBox="0 0 16 26"><polyline points="13,2 3,13 13,24" fill="none" stroke="#231a17" stroke-width="3"/></svg>
<svg class="abs arrow" style="left:785px" width="16" height="26" viewBox="0 0 16 26"><polyline points="3,2 13,13 3,24" fill="none" stroke="#231a17" stroke-width="3"/></svg>

<div class="abs card" style="left:43px">
  <div class="card-photo" role="img" aria-label="White mansion with a swimming pool" style="background:linear-gradient(180deg,#8fb3de,#e8e8e8 45%,#5f7f9e)"></div>
  <div class="card-title">Lorem ipsum dolor sit</div>
  <div class="card-meta"><span>3 Bed</span><span>$258.896</span></div>
  <span class="btn-gold details">Details</span>
</div>
<div class="abs divider" style="left:216px"></div>
<div class="abs card" style="left:235px">
  <div class="card-photo" role="img" aria-label="Mediterranean style villa with tiled roof and brick driveway" style="background:linear-gradient(180deg,#b9cfe4,#d8c2a6 45%,#9c6f5e)"></div>
  <div class="card-title">Lorem ipsum dolor sit</div>
  <div class="card-meta"><span>3 Bed</span><span>$258.896</span></div>
  <span class="btn-gold details">Details</span>
</div>
<div class="abs divider" style="left:407px"></div>
<div class="abs card" style="left:426px">
  <div class="card-photo" role="img" aria-label="Modern glass and brick office building" style="background:linear-gradient(180deg,#cfdff0,#8a8e92 45%,#6c6a66)"></div>
  <div class="card-title">Lorem ipsum dolor sit</div>
  <div class="card-meta"><span>3 Bed</span><span>$258.896</span></div>
  <span class="btn-gold details">Details</span>
</div>
<div class="abs divider" style="left:598px"></div>
<div class="abs card" style="left:617px">
  <div class="card-photo" role="img" aria-label="Contemporary mid-rise apartment building on a city street" style="background:linear-gradient(180deg,#5f8fd0,#9eb6cf 45%,#6e6a68)"></div>
  <div class="card-title">Lorem ipsum dolor sit</div>
  <div class="card-meta"><span>3 Bed</span><span>$258.896</span></div>
  <span class="btn-gold details">Details</span>
</div>

<footer class="abs footer"></footer>
<div class="abs likes"><span>Like</span>1,245 Likes</div>
<div class="abs copyright">© 2012 Dwell Vantoro - Terms of Service - Privacy Policy - Program Policies</div>

</body>
</html>
```